Finance cashflow waterfall graphic

Recreate "Cashflow Waterfall Example 1" - waterfall term used to explain the different accounts and priority that need to be paid as part of a apartment building / project. Create simple, business professional graphic for real estate report. Check the inspiration image but change to dorm building, no people - potentially combine the two images... Ideally editable so I can change the names of the accounts / colors / etc.

```html
<!DOCTYPE html>
<html lang="en">
<head>
<meta charset="utf-8">
<title>Waterfall Chart</title>
<link rel="stylesheet" href="https://fonts.googleapis.com/css2?family=Montserrat:wght@400;700&family=Source+Sans+3:wght@400;700&display=swap">
<style>
  :root {
    --ink: #111111;
    --paper: #f7f7f7;
    --swoosh: #e6e6e6;
    --step-revenue: #0e7470;
    --step-operating: #5d8a7a;
    --step-debt: #99a283;
    --step-asset: #dfc78b;
    --step-recap: #c4a06c;
    --step-incentive: #9b6b46;
    --banner-incentive: #5d8a7a;
    --step-final: #8b5232;
    --banner-text-light: #ffffff;
    --banner-text-dark: #1a1a1a;
  }
  html, body { margin: 0; padding: 0; overflow: hidden; }
  .canvas {
    position: relative;
    width: 1200px; height: 927px; overflow: hidden;
    background:
      radial-gradient(ellipse 520px 300px at 1050px 120px, var(--swoosh), transparent 70%),
      radial-gradient(ellipse 420px 260px at 80px 900px, var(--swoosh), transparent 70%),
      var(--paper);
    font-family: "Source Sans 3", Arial, sans-serif;
    color: var(--ink);
  }
  .title {
    position: absolute; right: 52px; top: 40px; margin: 0;
    font-family: "Montserrat", Arial, sans-serif;
    font-size: 45px; font-weight: 400; letter-spacing: 0.5px;
  }
  .title strong { font-weight: 700; }
  .intro {
    position: absolute; left: 672px; top: 100px; width: 476px; margin: 0;
    font-size: 15.5px; line-height: 20px; text-align: justify;
  }
  .step-line {
    position: absolute; height: 0; border-top: 2px solid var(--ink);
  }
  .step-line::after {
    content: ""; position: absolute; right: -4px; top: -5px;
    width: 8px; height: 8px; border-radius: 50%; background: var(--ink);
  }
  .building {
    position: absolute; width: 104px; height: 115px;
    background: var(--c); border: 2px solid var(--ink); box-sizing: border-box;
  }
  .faucet {
    position: absolute; width: 72px; height: 72px;
    background: linear-gradient(180deg, var(--c) 0 40%, transparent 40%),
                radial-gradient(circle at 62px 62px, var(--c) 0 9px, transparent 10px);
    opacity: 0.9;
  }
  .banner {
    position: absolute; display: flex; align-items: center; justify-content: center;
    text-align: center; box-sizing: border-box; padding-bottom: 4px;
    background: var(--c); color: var(--t, var(--banner-text-light));
    clip-path: polygon(0 0, 100% 0, 100% 100%, 50% 91%, 0 100%);
    font-family: "Montserrat", Arial, sans-serif; font-weight: 700;
    font-size: 18px; line-height: 21px; letter-spacing: 0.3px; text-transform: uppercase;
  }
  .banner--revenue { font-size: 22px; }
  .outcome {
    position: absolute; margin: 0;
    font-family: "Montserrat", Arial, sans-serif; font-weight: 700;
    font-size: 17.5px; line-height: 21px; text-transform: uppercase;
  }
  .outcome--reserves { right: 479px; top: 788px; text-align: right; }
  .outcome--returns { left: 942px; top: 792px; }
</style>
</head>
<body>
<main class="canvas">
  <h1 class="title"><strong>Waterfall</strong> Chart</h1>
  <p class="intro">Lorem ipsum dolor sit amet, consectetuer adipiscing elit, sed diam nonummy nibh euismod tincidunt ut laoreet dolore magna aliquam erat volutpat. Ut wisi enim ad minim veniam, quis nostrud exerci tation ullamcorper suscipit lobortis nisl ut aliquip ex ea commodo consequat. Duis autem vel eum iriure dolor in hendrerit in vulputate velit esse molestie consequat, vel illum dolore eu feugiat nulla facilisis at vero eros et accumsan et iusto odio dignissim qui blandit praesent luptatum zzril delenit augue duis dolore te feugait nulla facilisi.</p>

  <!-- Revenue -->
  <div class="step-line" style="left:51px;top:72px;width:305px"></div>
  <div class="building" style="--c:var(--step-revenue);left:57px;top:73px" role="img" aria-label="Dorm building icon with flag"></div>
  <div class="faucet" style="--c:var(--step-revenue);left:161px;top:105px" role="img" aria-label="Faucet dripping into next step"></div>
  <div class="banner banner--revenue" style="--c:var(--step-revenue);left:213px;top:73px;width:127px;height:42px">Revenue</div>

  <!-- Operating expenses -->
  <div class="step-line" style="left:56px;top:187px;width:426px"></div>
  <div class="building" style="--c:var(--step-operating);left:173px;top:188px" role="img" aria-label="Dorm building icon"></div>
  <div class="faucet" style="--c:var(--step-operating);left:267px;top:220px" role="img" aria-label="Faucet dripping into next step"></div>
  <div class="banner" style="--c:var(--step-operating);left:340px;top:188px;width:127px;height:57px">Operating<br>Expenses</div>

  <!-- Debt payment -->
  <div class="step-line" style="left:167px;top:302px;width:417px"></div>
  <div class="building" style="--c:var(--step-debt);left:285px;top:303px" role="img" aria-label="Dorm building icon"></div>
  <div class="faucet" style="--c:var(--step-debt);left:379px;top:335px" role="img" aria-label="Faucet dripping into next step"></div>
  <div class="banner" style="--c:var(--step-debt);left:458px;top:303px;width:103px;height:56px">Debt<br>Payment</div>

  <!-- Asset management fee -->
  <div class="step-line" style="left:279px;top:417px;width:468px"></div>
  <div class="building" style="--c:var(--step-asset);left:397px;top:418px" role="img" aria-label="Dorm building icon"></div>
  <div class="faucet" style="--c:var(--step-asset);left:491px;top:450px" role="img" aria-label="Faucet dripping into next step"></div>
  <div class="banner" style="--c:var(--step-asset);--t:var(--banner-text-dark);left:576px;top:418px;width:156px;height:77px">Asset<br>Management<br>Fee</div>

  <!-- Recapitalization accounts -->
  <div class="step-line" style="left:391px;top:532px;width:511px"></div>
  <div class="building" style="--c:var(--step-recap);left:509px;top:533px" role="img" aria-label="Dorm building icon"></div>
  <div class="faucet" style="--c:var(--step-recap);left:603px;top:565px" role="img" aria-label="Faucet dripping into next step"></div>
  <div class="banner" style="--c:var(--step-recap);left:688px;top:533px;width:199px;height:59px">Recapitalization<br>Accounts</div>

  <!-- Incentive fees -->
  <div class="step-line" style="left:503px;top:647px;width:434px"></div>
  <div class="building" style="--c:var(--step-incentive);left:621px;top:648px" role="img" aria-label="Dorm building icon"></div>
  <div class="faucet" style="--c:var(--step-incentive);left:715px;top:680px" role="img" aria-label="Faucet dripping into next step"></div>
  <div class="banner" style="--c:var(--banner-incentive);left:793px;top:648px;width:128px;height:58px">Incentive<br>Fees</div>

  <!-- Final distribution -->
  <div class="step-line" style="left:615px;top:762px;width:222px"></div>
  <div class="building" style="--c:var(--step-final);left:733px;top:764px;width:104px;height:116px" role="img" aria-label="Dorm building icon for member distribution"></div>
  <div class="building" style="--c:var(--step-final);left:848px;top:788px;width:87px;height:92px" role="img" aria-label="Smaller dorm building icon for managing member distribution"></div>
  <p class="outcome outcome--reserves">Sustainment Reserves/<br>Member Distribution<br>(60%)</p>
  <p class="outcome outcome--returns">Private Returns/<br>Managing Member<br>Distribution<br>(40%)</p>
</main>
</body>
</html>
```